Anchored Willow Website

Would like a website designed for my fitness and nutrition coaching company Anchor Willow. I have a company logo and would like to keep the page layout clean and simple. Needs to look great on computer and mobile devices.

Target Market(s)

Target market is individuals looking to make changes in their health and nutrition with the help of an online coach.

Industry/Entity Type

Fitness

Number of Pages Required

2 page

Colors
3176b5
0355a3
85acd3
cedeed
f8fcfd
ffffff

Requirements
Must have
• The first page should have the company logo and name towards the top and below that client before and after photos scrolling or displaying in some manner. Also would like a section that states services offered and a section about myself since I am the primary coach for clients.

```html
<!DOCTYPE html>
<html lang="en">
<head>
<meta charset="utf-8">
<title>Anchored Willow – Fitness &amp; Nutrition Coaching</title>
<link rel="stylesheet" href="https://fonts.googleapis.com/css2?family=Open+Sans:wght@400;600;700&family=Montserrat:wght@500;600;700&display=swap">
<style>
:root{
  --blue:#3176b5;
  --navy:#0355a3;
  --sky:#85acd3;
  --pale:#cedeed;
  --mist:#f8fcfd;
  --white:#ffffff;
  --ink:#333a44;
  --muted:#6d7480;
  --line:#d6dbe1;
}
*{box-sizing:border-box;margin:0;padding:0}
html,body{width:1200px;height:3719px;overflow:hidden}
body{position:relative;background:var(--white);font-family:"Open Sans",Arial,sans-serif;color:var(--ink)}
.abs{position:absolute}
.heading{font-family:"Montserrat",Arial,sans-serif;font-weight:700;color:var(--blue);text-align:center;font-size:48px;width:1200px;left:0}
.lede{left:0;width:1200px;text-align:center;font-size:13px;color:var(--muted);line-height:20px}

/* hero (drawn first so the header sits on top) */
.hero{top:0;left:0;width:1200px;height:625px;background:linear-gradient(180deg,#ffffff 0%,#f3f7fb 14%,#cfe0ee 26%,#a9c9e2 45%,#6f9fc4 60%,#d9c6a4 74%,#c9b08a 100%)}

/* header */
.header-band{top:0;left:0;width:1200px;height:54px;border-bottom:3px solid var(--blue);background:var(--white);z-index:2}
.top-contact{top:14px;left:752px;font-size:15px;color:var(--navy);display:flex;align-items:center;gap:14px;z-index:3}
.login-tab{top:0;left:930px;width:200px;height:56px;z-index:3}
.brand{top:96px;left:74px;display:flex;align-items:center;gap:10px;z-index:3}
.brand-square{width:22px;height:22px;background:var(--blue)}
.brand-name{font-family:"Montserrat",Arial,sans-serif;font-weight:700;font-size:19px;color:var(--blue);letter-spacing:.5px}
.main-nav{top:90px;left:460px;display:flex;font-size:15px;z-index:3}
.main-nav a{color:var(--ink);text-decoration:none;display:block;text-align:center;height:28px;line-height:28px}
.main-nav a.active{color:var(--white);background:var(--sky);padding:0 12px;margin-right:30px}

.hero-title{top:246px;left:100px;font-family:"Montserrat",Arial,sans-serif;font-weight:700;font-size:50px;color:var(--blue);letter-spacing:1px}
.hero-sub{top:308px;left:100px;font-size:30px;color:var(--ink)}
.hero-copy{top:364px;left:100px;width:475px;font-size:14px;line-height:19px;color:#1d2430}
.hero-btn{top:451px;left:100px;width:252px;height:52px;background:var(--blue);color:var(--white);font-weight:600;font-size:19px;display:flex;align-items:center;justify-content:center;letter-spacing:.5px}
.hero-arrow{top:336px;width:56px;height:110px}

.ba-card{top:607px;width:312px;height:174px;background:linear-gradient(120deg,#5b5048,#8a7466 50%,#3f3a3a);box-shadow:0 6px 12px rgba(0,0,0,.25)}
.ba-card span{position:absolute;top:12px;font-weight:700;font-size:17px;color:var(--white)}

/* services */
.svc{width:290px}
.svc h3{font-weight:400;font-size:18px;color:var(--blue);padding-bottom:12px;border-bottom:1px solid var(--line)}
.svc p{font-size:13px;color:var(--muted);line-height:20px;margin-top:10px}
.svc.left{text-align:right}
.svc.left h3,.svc.left p{padding-right:12px;border-right:1px solid var(--line)}
.svc.right h3,.svc.right p{padding-left:12px;border-left:1px solid var(--line)}
.coach-photo{top:1054px;left:338px;width:520px;height:410px;background:radial-gradient(ellipse at 50% 45%,#d9c4b3 0%,#bfa896 30%,#ececec 60%,#ffffff 78%)}

/* about */
.about{top:1544px;left:0;width:1200px;height:365px;background:linear-gradient(90deg,#2f72b2 0%,#3a82c2 55%,#5c98cc 100%)}
.about-title{top:1608px;left:80px;font-family:"Montserrat",Arial,sans-serif;font-weight:700;font-size:46px;color:var(--white)}
.about-copy{top:1690px;left:80px;width:560px;font-size:15px;line-height:23px;color:#e6f0fa}
.about-btn{top:1805px;left:79px;width:194px;height:49px;background:var(--white);color:var(--blue);font-weight:700;font-size:17px;display:flex;align-items:center;justify-content:center}

/* testimonial */
.client-name{top:2278px;left:0;width:1200px;text-align:center;font-size:24px;color:var(--ink)}
.quote{top:2320px;left:200px;width:800px;text-align:center;font-style:italic;font-size:13px;line-height:21px;color:var(--muted)}
.quote-edge{top:2318px;font-style:italic;font-size:13px;line-height:21px;color:var(--sky);width:160px}

/* gallery */
.tile{position:absolute}

/* contact */
.field{font-size:13px;color:var(--muted);border-bottom:1px solid var(--line);padding-bottom:12px}
.submit{top:3329px;left:508px;width:184px;height:47px;background:var(--blue);color:var(--white);font-weight:700;font-size:18px;display:flex;align-items:center;justify-content:center;letter-spacing:1px}
.write{top:3393px;left:0;width:1200px;text-align:center;font-size:28px;color:var(--blue);text-decoration:underline;text-underline-offset:4px}
.mail-line{top:3440px;left:0;width:1200px;display:flex;justify-content:center;align-items:center;gap:12px;font-size:15px;color:var(--blue)}

/* footer */
.footer{top:3508px;left:0;width:1200px;height:211px;background:var(--blue)}
.foot-nav{top:3550px;left:80px;display:flex;gap:46px;font-size:13px;color:var(--white)}
.foot-rule{top:3601px;left:80px;width:1040px;height:1px;background:rgba(255,255,255,.45)}
.foot-item{display:flex;align-items:center;gap:16px;color:var(--white);font-size:13px;line-height:18px}
.foot-icon{width:50px;height:50px;border-radius:50%;border:1px solid rgba(255,255,255,.6);display:flex;align-items:center;justify-content:center}
.foot-icon.solid{background:var(--sky);border:none}
.copy{top:3640px;left:860px;width:270px;text-align:right;font-size:13px;color:var(--white);line-height:18px}
.copy b{font-weight:700}
</style>
</head>
<body>

<!-- hero background -->
<div class="abs hero" role="img" aria-label="Photo of a man and a woman jogging along a sunny beach"></div>

<!-- header -->
<div class="abs header-band"></div>
<div class="abs top-contact">
  <svg width="16" height="16" viewBox="0 0 16 16"><circle cx="6.5" cy="6.5" r="4.5" fill="none" stroke="#0355a3" stroke-width="2"/><path d="M10 10l4 4" stroke="#0355a3" stroke-width="2"/></svg>
  <span style="display:flex;align-items:center;gap:6px">
    <svg width="15" height="15" viewBox="0 0 16 16"><path d="M3 1l3 0 1 4-2 1.5c1 2 2.5 3.5 4.5 4.5L11 9l4 1v3c0 1-1 2-2 2C7 15 1 9 1 3c0-1 1-2 2-2z" fill="#0355a3"/></svg>
    555 014 7878
  </span>
</div>
<svg class="abs login-tab" viewBox="0 0 200 56">
  <path d="M0 0H200L170 40 100 56 30 40Z" fill="#ffffff" stroke="#3176b5" stroke-width="3"/>
  <text x="100" y="24" text-anchor="middle" font-family="Open Sans, sans-serif" font-size="16" fill="#333a44">LOGIN</text>
  <path d="M93 32l7 5 7-5M93 38l7 5 7-5" fill="none" stroke="#0355a3" stroke-width="2"/>
</svg>
<div class="abs brand"><div class="brand-square"></div><div class="brand-name">ANCHORED WILLOW</div></div>
<nav class="abs main-nav">
  <a class="active" href="#">Home</a>
  <a href="#" style="width:106px">About</a>
  <a href="#" style="width:106px">Services</a>
  <a href="#" style="width:106px">Gallery</a>
  <a href="#" style="width:136px">Testimonial</a>
  <a href="#" style="width:126px">Contact Us</a>
</nav>

<!-- hero content -->
<div class="abs hero-title">HARBOR WELLNESS</div>
<div class="abs hero-sub">Health &amp; Happiness</div>
<p class="abs hero-copy">Lorem Ipsum is simply dummy text of the printing and typesetting industry. Lorem Ipsum has been the industry's standard dummy text ever since the 1500...</p>
<div class="abs hero-btn">GET STARTED</div>
<svg class="abs hero-arrow" style="left:0" viewBox="0 0 56 110"><path d="M0 0L56 55 0 110Z" fill="#3176b5"/><path d="M22 47l-8 8 8 8M31 47l-8 8 8 8" fill="none" stroke="#fff" stroke-width="3"/></svg>
<svg class="abs hero-arrow" style="left:1144px" viewBox="0 0 56 110"><path d="M56 0L0 55 56 110Z" fill="#3176b5"/><path d="M34 47l8 8-8 8M25 47l8 8-8 8" fill="none" stroke="#fff" stroke-width="3"/></svg>

<div class="abs ba-card" style="left:77px" role="img" aria-label="Client before and after photos, woman in pink top"><span style="left:75px">BEFORE</span><span style="left:168px">AFTER</span></div>
<div class="abs ba-card" style="left:444px" role="img" aria-label="Client before and after photos, shirtless man"><span style="left:75px">BEFORE</span><span style="left:168px">AFTER</span></div>
<div class="abs ba-card" style="left:811px" role="img" aria-label="Client before and after photos, woman in sports top"><span style="left:75px">BEFORE</span><span style="left:168px">AFTER</span></div>

<!-- what we do -->
<h2 class="abs heading" style="top:848px">What We Do</h2>
<p class="abs lede" style="top:927px">Do you feel like you can't keep up with the latest nutrition news because it's always changing? While it's true that what is known<br>about nutrition and diet is evolving, there are some nutrition basics that can help you sort through the latest research and advice.</p>

<div class="abs coach-photo" role="img" aria-label="Smiling man doing a push-up with an armband music player"></div>

<div class="abs svc left" style="top:1044px;left:58px"><h3>Services.01</h3><p>The best contact you will get here<br>lorem ipsum dolor sit amet</p></div>
<div class="abs svc left" style="top:1212px;left:9px"><h3>Serviece.02</h3><p>The best contact you will get here<br>lorem ipsum dolor sit amet</p></div>
<div class="abs svc left" style="top:1381px;left:52px"><h3>Service.03</h3><p>The best contact you will get here<br>lorem ipsum dolor sit amet</p></div>
<div class="abs svc right" style="top:1044px;left:840px"><h3>04. Service</h3><p>The best contact you will get here<br>lorem ipsum dolor sit amet</p></div>
<div class="abs svc right" style="top:1212px;left:893px"><h3>05. Service</h3><p>The best contact you will get here<br>lorem ipsum dolor sit amet</p></div>
<div class="abs svc right" style="top:1381px;left:866px"><h3>06. Service</h3><p>The best contact you will get here<br>lorem ipsum dolor sit amet</p></div>

<!-- about -->
<section class="abs about"></section>
<h2 class="abs about-title">About Anchored Willow</h2>
<p class="abs about-copy">Lorem Ipsum is simply dummy text of the printing and typesetting industry. Lorem Ipsum has been the industry's standard dummy text ever since the 1500s, when an unknown printer took a galley.Lorem Ipsum is simply dummy text of the printing and typesetting industry.</p>
<div class="abs about-btn">READ MORE</div>
<svg class="abs" style="top:1560px;left:650px" width="550" height="340" viewBox="0 0 550 340" role="img" aria-label="Diamond photos of healthy food, fruit, nuts and a muscular man">
  <path d="M95 115l85 85-85 85-85-85Z" fill="#c77a3a"/>
  <path d="M243 12l40 40-40 40-40-40Z" fill="#c9a35a"/>
  <path d="M416 24l115 115-115 115-115-115Z" fill="#3a2a26"/>
  <path d="M292 173l40 40-40 40-40-40Z" fill="#8fcf5a"/>
</svg>

<!-- testimonial -->
<h2 class="abs heading" style="top:1972px">Testimonial</h2>
<p class="abs lede" style="top:2054px">What our client Say</p>
<svg class="abs" style="top:2102px;left:440px" width="320" height="160" viewBox="0 0 320 160">
  <path d="M160 4l76 76-76 76-76-76Z" fill="#9a7a68" role="img" aria-label="Client portrait"/>
  <path d="M38 68l12 12-12 12-12-12Z" fill="none" stroke="#3176b5" stroke-width="2"/>
  <path d="M41 80h-8m3-3l-3 3 3 3" fill="none" stroke="#3176b5" stroke-width="1.6"/>
  <path d="M276 68l12 12-12 12-12-12Z" fill="none" stroke="#333a44" stroke-width="2"/>
  <path d="M272 80h8m-3-3l3 3-3 3" fill="none" stroke="#333a44" stroke-width="1.6"/>
</svg>
<div class="abs client-name">- Client Name</div>
<p class="abs quote">"Lorem Ipsum is simply dummy text of the printing and typesetting industry. Lorem Ipsum has been the industry's standard dummy text ever since the 1500s, when an unknown printer took a galley of type and scrambled it to make a type specimen book.Lorem Ipsum is simply dummy text."</p>
<div class="abs" style="top:2256px;left:160px;width:1px;height:160px;background:var(--line)"></div>
<div class="abs" style="top:2256px;left:1058px;width:1px;height:160px;background:var(--line)"></div>
<p class="abs quote-edge" style="left:0;text-align:right;width:80px">y's standard<br>e specimen</p>
<p class="abs quote-edge" style="left:1118px">"Lorem<br>dummy text</p>

<!-- gallery -->
<div class="tile" style="top:2467px;left:0;width:478px;height:260px;background:linear-gradient(135deg,#3a4f7a,#6e86a8 60%,#c9c9c9)" role="img" aria-label="Woman exercising on a fitness ball"></div>
<div class="tile" style="top:2467px;left:478px;width:241px;height:520px;background:linear-gradient(180deg,#c7d5e2,#9fb7cc);border:7px solid var(--blue)" role="img" aria-label="Highlighted gallery photo of a yoga pose"></div>
<svg class="abs" style="top:2687px;left:578px" width="42" height="42"><path d="M21 0v42M0 21h42" stroke="#333a44" stroke-width="1.5"/></svg>
<div class="tile" style="top:2467px;left:719px;width:240px;height:260px;background:linear-gradient(135deg,#e8dcd2,#a6b6c9)" role="img" aria-label="Woman lifting light dumbbells"></div>
<div class="tile" style="top:2467px;left:959px;width:241px;height:260px;background:linear-gradient(135deg,#efefef,#b8958a)" role="img" aria-label="Gymnast in a handstand on bars"></div>
<div class="tile" style="top:2727px;left:0;width:240px;height:260px;background:linear-gradient(135deg,#2e2e34,#8c8a3a)" role="img" aria-label="Woman training on gymnastic rings"></div>
<div class="tile" style="top:2727px;left:240px;width:238px;height:260px;background:linear-gradient(135deg,#f0ebe6,#8a7c72)" role="img" aria-label="Woman stretching in a studio"></div>
<div class="tile" style="top:2727px;left:719px;width:481px;height:260px;background:linear-gradient(135deg,#e9e5e0,#6c6460 60%,#d8d2cc)" role="img" aria-label="Group of women in a yoga class"></div>

<!-- contact -->
<h2 class="abs heading" style="top:3050px">Contact Us</h2>
<p class="abs lede" style="top:3131px">If you have any questions about how we can help you please either send us an email or call us on below details...</p>
<div class="abs field" style="top:3186px;left:317px;width:278px">Name</div>
<div class="abs field" style="top:3186px;left:612px;width:275px">Email Id</div>
<div class="abs field" style="top:3237px;left:317px;width:570px;height:84px">Message...</div>
<div class="abs submit">SUBMIT</div>
<div class="abs write">Or Write &nbsp;to Email</div>
<div class="abs mail-line">
  <svg width="18" height="14" viewBox="0 0 18 14"><rect width="18" height="14" rx="1" fill="#0355a3"/><path d="M1 1l8 7 8-7" fill="none" stroke="#fff" stroke-width="1.5"/></svg>
  info@anchoredwillow.com
</div>

<!-- footer -->
<footer class="abs footer"></footer>
<nav class="abs foot-nav"><span>Home</span><span>About</span><span>Services</span><span>Gallery</span><span>Testimonial</span><span>Contact</span></nav>
<svg class="abs" style="top:3531px;left:955px" width="170" height="50" viewBox="0 0 170 50">
  <path d="M25 3l22 22-22 22L3 25Z" fill="#fff"/>
  <path d="M82 3l22 22-22 22-22-22Z" fill="none" stroke="#fff" stroke-width="1.5"/>
  <path d="M139 3l22 22-22 22-22-22Z" fill="none" stroke="#fff" stroke-width="1.5"/>
</svg>
<div class="abs foot-rule"></div>
<div class="abs foot-item" style="top:3636px;left:80px">
  <div class="foot-icon solid"><svg width="18" height="24" viewBox="0 0 18 24"><path d="M9 0a8 8 0 0 1 8 8c0 6-8 16-8 16S1 14 1 8a8 8 0 0 1 8-8z" fill="#0355a3"/><circle cx="9" cy="8" r="3" fill="#85acd3"/></svg></div>
  <span>123, Lorem ipsum dummy,<br>Country-123456.</span>
</div>
<div class="abs foot-item" style="top:3636px;left:342px">
  <div class="foot-icon"><svg width="18" height="18" viewBox="0 0 16 16"><path d="M3 1l3 0 1 4-2 1.5c1 2 2.5 3.5 4.5 4.5L11 9l4 1v3c0 1-1 2-2 2C7 15 1 9 1 3c0-1 1-2 2-2z" fill="#fff"/></svg></div>
  <span>555 014 7878</span>
</div>
<div class="abs foot-item" style="top:3636px;left:597px">
  <div class="foot-icon"><svg width="20" height="15" viewBox="0 0 18 14"><rect width="18" height="14" rx="1" fill="#fff"/><path d="M1 1l8 7 8-7" fill="none" stroke="#3176b5" stroke-width="1.5"/></svg></div>
  <span>info@anchoredwillow.com</span>
</div>
<div class="abs copy">© <b>ANCHORED WILLOW</b> - 2017<br>All rights reserved.</div>

</body>
</html>
```